Website redesign for job agency recruitment

Please refer to the attached document, “Harbor Work Portal Outline,” for comprehensive details regarding the scope, objectives, and requirements of this website redesign project.

For imagery you can use images from this website https://www.pixvaultmedia.com or any other you regularly use.

Target Market(s)

Jobseekers and Companies looking for general labour

Industry/Entity Type

Services: Oil, Gas and Mining, Administrative, Construction and Trades, Warehouse and Logistics and, Manufacturing.

Number of Pages Required

5+ page

Font styles to use
Serif
Other font styles liked:
• Inter, Open-Sans or similar.

Requirements
Must have
• The requirements highlighted in the Word document attached. The final design needs to be provided in Figma including all viewports (Desktop, mobiel and tablet)
Should not have
• Website we like as a reference: www.beltonworkforceinc.com, www.veltaworkforce.com, www.zplacer.com, www.brimwellworkforce.com, www.9tworkcrew.com, www.hiringonthemove.ca

```html
<!DOCTYPE html>
<html lang="en">
<head>
<meta charset="utf-8">
<title>Harborline Recruitment — Candidates</title>
<link href="https://fonts.googleapis.com/css2?family=Inter:wght@300;400;500;600;700&family=Plus+Jakarta+Sans:wght@600;700;800&display=swap" rel="stylesheet">
<style>
:root{
  --navy:#1c2a6b;
  --navy-deep:#17235c;
  --ink:#1a2455;
  --text:#5a6278;
  --muted:#8b92a5;
  --yellow:#fcc42c;
  --gold:#c9940f;
  --line:#e6e9f0;
  --soft:#f7f8fb;
  --white:#ffffff;
  --green:#16a34a;
  --green-bg:#e8f7ee;
  --blue:#2f56d6;
  --blue-bg:#e9eefc;
  --pink:#c026d3;
  --pink-bg:#fbeafd;
  --orange:#d97706;
  --orange-bg:#fdf3e2;
}
*{box-sizing:border-box;margin:0;padding:0}
html,body{width:1200px;height:2604px;overflow:hidden}
body{font-family:"Inter",sans-serif;color:var(--text);background:var(--white)}
.wrap{width:800px;margin:0 auto;position:relative}
h1,h2,h3,.display{font-family:"Plus Jakarta Sans",sans-serif}

/* nav */
.nav{height:64px;background:#e9ebf1}
.nav .wrap{display:flex;align-items:center;height:64px}
.brand{display:flex;align-items:center;gap:8px;font-weight:700;font-size:14px;color:var(--navy)}
.brand-dot{width:12px;height:12px;border-radius:50%;background:var(--yellow)}
.nav-links{margin-left:auto;display:flex;align-items:center;gap:22px;font-size:12px;color:var(--ink)}
.btn-sm{padding:8px 14px;border-radius:5px;font-weight:600;font-size:12px}
.btn-yellow{background:var(--yellow);color:var(--ink)}
.btn-navy{background:var(--navy);color:var(--white)}

/* hero */
.hero{height:385px;background:radial-gradient(circle at 98% 8%,rgba(255,255,255,.12),transparent 180px),var(--navy);padding-top:74px}
.tag{display:inline-flex;align-items:center;gap:6px;background:rgba(255,255,255,.14);color:var(--yellow);font-size:8.5px;font-weight:700;letter-spacing:.8px;padding:5px 11px;border-radius:12px}
.hero h1{color:var(--white);font-size:40px;line-height:40px;font-weight:800;margin-top:14px}
.hero h1 span{color:var(--yellow)}
.hero p{color:#b7bfdc;font-size:12.5px;line-height:20px;width:380px;margin-top:16px;font-weight:300}
.hero-actions{display:flex;gap:11px;margin-top:27px}
.btn{display:inline-flex;align-items:center;gap:7px;height:38px;padding:0 22px;border-radius:6px;font-weight:600;font-size:11.5px}
.btn-hero{background:var(--yellow);color:var(--ink);box-shadow:0 6px 14px rgba(252,196,44,.3)}
.btn-ghost{background:rgba(255,255,255,.1);border:1px solid rgba(255,255,255,.3);color:var(--white)}

/* section heads */
.eyebrow{font-size:9px;font-weight:700;letter-spacing:1.3px;color:var(--gold)}
.sec-title{font-size:24px;font-weight:800;color:var(--ink);margin-top:6px}
.center{text-align:center}

/* how */
.how{height:411px;padding-top:66px}
.how .lead{font-size:12px;color:var(--text);margin-top:12px;font-weight:300}
.steps{display:grid;grid-template-columns:repeat(4,1fr);gap:16px;margin-top:44px}
.step{height:164px;background:var(--soft);border:1px solid #eef0f5;border-radius:9px;padding:19px 19px;position:relative}
.step.active{border-color:#f4d98a;background:#fbfbfd}
.step-num{width:29px;height:29px;border-radius:6px;background:var(--navy);color:var(--yellow);font-size:9px;font-weight:700;display:flex;align-items:center;justify-content:center}
.step-ghost{position:absolute;right:16px;top:14px;font-family:"Plus Jakarta Sans",sans-serif;font-weight:800;font-size:24px;color:#dfe3ee}
.step.active .step-ghost{color:#fbd98c}
.step h3{font-size:11px;font-weight:700;color:var(--ink);margin-top:16px}
.step p{font-size:9px;line-height:15px;margin-top:8px}

/* roles */
.roles{height:726px;background:var(--soft);padding-top:66px}
.filters{display:flex;gap:8px;justify-content:center;margin-top:24px}
.search{width:304px;height:30px;background:var(--white);border:1px solid var(--line);border-radius:6px;display:flex;align-items:center;gap:7px;padding:0 10px;font-size:9px;color:#a3a9b9}
.select{width:137px;height:30px;background:var(--white);border:1px solid var(--line);border-radius:6px;display:flex;align-items:center;justify-content:space-between;padding:0 10px;font-size:9px;color:var(--ink)}
.grid{display:grid;grid-template-columns:repeat(3,1fr);gap:14px;margin-top:22px}
.job{height:147px;background:var(--white);border:1px solid var(--line);border-radius:9px;padding:16px 16px}
.job-top{display:flex;justify-content:space-between;align-items:flex-start}
.job h3{font-size:11px;font-weight:700;color:var(--ink)}
.job .sector{font-size:9px;color:var(--muted);margin-top:5px}
.pill{font-size:7.5px;font-weight:600;padding:3px 7px;border-radius:4px}
.perm{background:var(--green-bg);color:var(--green)}
.contract{background:var(--blue-bg);color:var(--blue)}
.ttp{background:var(--pink-bg);color:var(--pink)}
.temp{background:var(--orange-bg);color:var(--orange)}
.meta{display:flex;align-items:center;gap:6px;font-size:9px;color:var(--text);margin-top:8px}
.meta:first-of-type{margin-top:15px}
.apply{margin-top:12px;height:27px;border:1px solid #c9cee0;border-radius:5px;display:flex;align-items:center;justify-content:center;font-size:9.5px;font-weight:600;color:var(--ink)}

/* benefits */
.benefits{height:511px;padding-top:68px}
.benefits .wrap{display:flex;justify-content:space-between}
.ben-left{width:380px}
.ben-left .sec-title{font-size:24px;line-height:27px}
.ben-list{margin-top:18px;list-style:none}
.ben-list li{display:flex;gap:11px;margin-bottom:17px}
.tick{flex:none;width:21px;height:21px;border-radius:5px;background:#fdf0c9;display:flex;align-items:center;justify-content:center}
.ben-list h3{font-family:"Inter",sans-serif;font-size:11px;font-weight:600;color:var(--ink)}
.ben-list p{font-size:9px;line-height:15px;margin-top:3px}
.ben-photo{width:379px;height:307px;margin-top:34px;border-radius:9px;background:linear-gradient(135deg,#e9eaec 0%,#f5f5f5 45%,#c9cbcf 80%,#3b3d42 100%);box-shadow:0 12px 28px rgba(28,42,107,.12)}

/* cta */
.cta{height:269px;background:radial-gradient(circle at 98% 6%,rgba(255,255,255,.1),transparent 160px),var(--navy);text-align:center;padding-top:64px}
.cta h2{color:var(--white);font-size:24px;font-weight:800}
.cta p{color:#b7bfdc;font-size:12px;line-height:19px;width:380px;margin:14px auto 0;font-weight:300}
.cta .btn{margin-top:26px;height:37px;padding:0 26px}

/* footer */
.footer{height:238px;background:var(--navy-deep);padding-top:46px}
.foot-cols{display:grid;grid-template-columns:repeat(4,1fr);height:138px}
.foot-brand{display:flex;align-items:center;gap:6px;font-weight:700;font-size:12px;color:var(--white)}
.foot-about{font-size:9px;line-height:15px;color:#8f98c0;margin-top:16px;width:185px}
.foot-cols h4{font-size:9px;font-weight:700;letter-spacing:1px;color:var(--yellow)}
.foot-cols ul{list-style:none;margin-top:12px}
.foot-cols li{font-size:9px;color:#a6aed0;margin-bottom:10px}
.foot-bottom{border-top:1px solid rgba(255,255,255,.1);display:flex;justify-content:space-between;padding-top:16px;font-size:7.5px;color:#7c86b3}
.foot-bottom span+span{margin-left:16px}
</style>
</head>
<body>

<header class="nav">
  <div class="wrap">
    <div class="brand"><span class="brand-dot"></span>Harborline</div>
    <nav class="nav-links">
      <span>Home</span><span>Sectors</span><span>Browse Jobs</span><span>How It Works</span>
      <span class="btn-sm btn-yellow">Candidates</span>
      <span class="btn-sm btn-navy">Employers</span>
    </nav>
  </div>
</header>

<section class="hero">
  <div class="wrap">
    <span class="tag">
      <svg width="9" height="9" viewBox="0 0 10 10" fill="none" stroke="currentColor" stroke-width="1.2"><circle cx="5" cy="3" r="2"/><path d="M1.5 9c.5-2 2-3 3.5-3s3 1 3.5 3"/></svg>
      FOR CANDIDATES
    </span>
    <h1>Find Your Next<br><span>Opportunity</span></h1>
    <p>Browse live vacancies across our specialist sectors. Register today and let our consultants match you with the right role.</p>
    <div class="hero-actions">
      <span class="btn btn-hero">Browse Jobs
        <svg width="10" height="10" viewBox="0 0 10 10" fill="none" stroke="currentColor" stroke-width="1.4"><path d="M5 1v8M1.8 5.8 5 9l3.2-3.2"/></svg>
      </span>
      <span class="btn btn-ghost">
        <svg width="12" height="12" viewBox="0 0 12 12" fill="none" stroke="currentColor" stroke-width="1.2"><path d="M3.5 9H3a2.3 2.3 0 0 1-.3-4.6A3.2 3.2 0 0 1 9 4.2 2.4 2.4 0 0 1 9 9h-.5"/><path d="M6 10.5V6M4.3 7.5 6 5.8l1.7 1.7"/></svg>
        Submit Your CV
      </span>
    </div>
  </div>
</section>

<section class="how">
  <div class="wrap center">
    <div class="eyebrow">SIMPLE PROCESS</div>
    <h2 class="sec-title">How It Works</h2>
    <p class="lead">From registration to placement — four straightforward steps.</p>
  </div>
  <div class="wrap steps">
    <div class="step"><div class="step-num">01</div><div class="step-ghost">01</div><h3>Register with Us</h3><p>Submit your CV and details through our quick registration form. It only takes a few minutes.</p></div>
    <div class="step"><div class="step-num">02</div><div class="step-ghost">02</div><h3>Speak to a Consultant</h3><p>A dedicated sector consultant will contact you to discuss your experience, skills and preferences.</p></div>
    <div class="step"><div class="step-num">03</div><div class="step-ghost">03</div><h3>Get Matched</h3><p>We match you with suitable roles from our active client vacancies — no generic job blasts.</p></div>
    <div class="step active"><div class="step-num">04</div><div class="step-ghost">04</div><h3>Start Working</h3><p>Once placed, we stay in touch to make sure everything is going smoothly in your new role.</p></div>
  </div>
</section>

<section class="roles">
  <div class="wrap center">
    <div class="eyebrow">LIVE VACANCIES</div>
    <h2 class="sec-title">Featured Roles</h2>
  </div>
  <div class="filters">
    <div class="search">
      <svg width="10" height="10" viewBox="0 0 10 10" fill="none" stroke="#9aa1b3" stroke-width="1.2"><circle cx="4.3" cy="4.3" r="3.2"/><path d="m6.7 6.7 2.5 2.5"/></svg>
      Search job title or location...
    </div>
    <div class="select">All Sectors
      <svg width="8" height="8" viewBox="0 0 8 8" fill="none" stroke="currentColor" stroke-width="1.2"><path d="m1.5 3 2.5 2.5L6.5 3"/></svg>
    </div>
  </div>
  <div class="wrap grid">
    <div class="job"><div class="job-top"><div><h3>Site Supervisor</h3><div class="sector">Construction &amp; Trades</div></div><span class="pill perm">Permanent</span></div>
      <div class="meta"><svg width="9" height="9" viewBox="0 0 10 10" fill="none" stroke="#b7bccb" stroke-width="1"><path d="M5 9s3-3 3-5a3 3 0 0 0-6 0c0 2 3 5 3 5z"/><circle cx="5" cy="4" r="1"/></svg>Manchester</div>
      <div class="meta"><svg width="9" height="9" viewBox="0 0 10 10" fill="none" stroke="#b7bccb" stroke-width="1"><circle cx="5" cy="5" r="4"/><path d="M5 2.5v5M6.3 3.6H4.5a.9.9 0 0 0 0 1.8h1a.9.9 0 0 1 0 1.8H3.7"/></svg>£38,000 – £45,000</div>
      <div class="apply">Apply Now</div></div>
    <div class="job"><div class="job-top"><div><h3>Warehouse Team Leader</h3><div class="sector">Warehouse &amp; Logistics</div></div><span class="pill perm">Permanent</span></div>
      <div class="meta"><svg width="9" height="9" viewBox="0 0 10 10" fill="none" stroke="#b7bccb" stroke-width="1"><path d="M5 9s3-3 3-5a3 3 0 0 0-6 0c0 2 3 5 3 5z"/><circle cx="5" cy="4" r="1"/></svg>Birmingham</div>
      <div class="meta"><svg width="9" height="9" viewBox="0 0 10 10" fill="none" stroke="#b7bccb" stroke-width="1"><circle cx="5" cy="5" r="4"/><path d="M5 2.5v5M6.3 3.6H4.5a.9.9 0 0 0 0 1.8h1a.9.9 0 0 1 0 1.8H3.7"/></svg>£28,000 – £32,000</div>
      <div class="apply">Apply Now</div></div>
    <div class="job"><div class="job-top"><div><h3>Rig Electrician</h3><div class="sector">Oil, Gas &amp; Mining</div></div><span class="pill contract">Contract</span></div>
      <div class="meta"><svg width="9" height="9" viewBox="0 0 10 10" fill="none" stroke="#b7bccb" stroke-width="1"><path d="M5 9s3-3 3-5a3 3 0 0 0-6 0c0 2 3 5 3 5z"/><circle cx="5" cy="4" r="1"/></svg>Aberdeen (FIFO)</div>
      <div class="meta"><svg width="9" height="9" viewBox="0 0 10 10" fill="none" stroke="#b7bccb" stroke-width="1"><circle cx="5" cy="5" r="4"/><path d="M5 2.5v5M6.3 3.6H4.5a.9.9 0 0 0 0 1.8h1a.9.9 0 0 1 0 1.8H3.7"/></svg>£350 – £420/day</div>
      <div class="apply">Apply Now</div></div>

    <div class="job"><div class="job-top"><div><h3>Office Manager</h3><div class="sector">Administrative</div></div><span class="pill perm">Permanent</span></div>
      <div class="meta"><svg width="9" height="9" viewBox="0 0 10 10" fill="none" stroke="#b7bccb" stroke-width="1"><path d="M5 9s3-3 3-5a3 3 0 0 0-6 0c0 2 3 5 3 5z"/><circle cx="5" cy="4" r="1"/></svg>London</div>
      <div class="meta"><svg width="9" height="9" viewBox="0 0 10 10" fill="none" stroke="#b7bccb" stroke-width="1"><circle cx="5" cy="5" r="4"/><path d="M5 2.5v5M6.3 3.6H4.5a.9.9 0 0 0 0 1.8h1a.9.9 0 0 1 0 1.8H3.7"/></svg>£32,000 – £38,000</div>
      <div class="apply">Apply Now</div></div>
    <div class="job"><div class="job-top"><div><h3>CNC Machine Operator</h3><div class="sector">Manufacturing</div></div><span class="pill ttp">Temp to Perm</span></div>
      <div class="meta"><svg width="9" height="9" viewBox="0 0 10 10" fill="none" stroke="#b7bccb" stroke-width="1"><path d="M5 9s3-3 3-5a3 3 0 0 0-6 0c0 2 3 5 3 5z"/><circle cx="5" cy="4" r="1"/></svg>Sheffield</div>
      <div class="meta"><svg width="9" height="9" viewBox="0 0 10 10" fill="none" stroke="#b7bccb" stroke-width="1"><circle cx="5" cy="5" r="4"/><path d="M5 2.5v5M6.3 3.6H4.5a.9.9 0 0 0 0 1.8h1a.9.9 0 0 1 0 1.8H3.7"/></svg>£14.50 – £17.00/hr</div>
      <div class="apply">Apply Now</div></div>
    <div class="job"><div class="job-top"><div><h3>Forklift Driver (Reach)</h3><div class="sector">Warehouse &amp; Logistics</div></div><span class="pill temp">Temporary</span></div>
      <div class="meta"><svg width="9" height="9" viewBox="0 0 10 10" fill="none" stroke="#b7bccb" stroke-width="1"><path d="M5 9s3-3 3-5a3 3 0 0 0-6 0c0 2 3 5 3 5z"/><circle cx="5" cy="4" r="1"/></svg>Bristol</div>
      <div class="meta"><svg width="9" height="9" viewBox="0 0 10 10" fill="none" stroke="#b7bccb" stroke-width="1"><circle cx="5" cy="5" r="4"/><path d="M5 2.5v5M6.3 3.6H4.5a.9.9 0 0 0 0 1.8h1a.9.9 0 0 1 0 1.8H3.7"/></svg>£13.00 – £15.50/hr</div>
      <div class="apply">Apply Now</div></div>

    <div class="job"><div class="job-top"><div><h3>Scaffolder (CISRS)</h3><div class="sector">Construction &amp; Trades</div></div><span class="pill contract">Contract</span></div>
      <div class="meta"><svg width="9" height="9" viewBox="0 0 10 10" fill="none" stroke="#b7bccb" stroke-width="1"><path d="M5 9s3-3 3-5a3 3 0 0 0-6 0c0 2 3 5 3 5z"/><circle cx="5" cy="4" r="1"/></svg>Leeds</div>
      <div class="meta"><svg width="9" height="9" viewBox="0 0 10 10" fill="none" stroke="#b7bccb" stroke-width="1"><circle cx="5" cy="5" r="4"/><path d="M5 2.5v5M6.3 3.6H4.5a.9.9 0 0 0 0 1.8h1a.9.9 0 0 1 0 1.8H3.7"/></svg>£200 – £260/day</div>
      <div class="apply">Apply Now</div></div>
    <div class="job"><div class="job-top"><div><h3>Executive Assistant</h3><div class="sector">Administrative</div></div><span class="pill perm">Permanent</span></div>
      <div class="meta"><svg width="9" height="9" viewBox="0 0 10 10" fill="none" stroke="#b7bccb" stroke-width="1"><path d="M5 9s3-3 3-5a3 3 0 0 0-6 0c0 2 3 5 3 5z"/><circle cx="5" cy="4" r="1"/></svg>Edinburgh</div>
      <div class="meta"><svg width="9" height="9" viewBox="0 0 10 10" fill="none" stroke="#b7bccb" stroke-width="1"><circle cx="5" cy="5" r="4"/><path d="M5 2.5v5M6.3 3.6H4.5a.9.9 0 0 0 0 1.8h1a.9.9 0 0 1 0 1.8H3.7"/></svg>£28,000 – £34,000</div>
      <div class="apply">Apply Now</div></div>
    <div class="job"><div class="job-top"><div><h3>Process Technician</h3><div class="sector">Manufacturing</div></div><span class="pill perm">Permanent</span></div>
      <div class="meta"><svg width="9" height="9" viewBox="0 0 10 10" fill="none" stroke="#b7bccb" stroke-width="1"><path d="M5 9s3-3 3-5a3 3 0 0 0-6 0c0 2 3 5 3 5z"/><circle cx="5" cy="4" r="1"/></svg>Coventry</div>
      <div class="meta"><svg width="9" height="9" viewBox="0 0 10 10" fill="none" stroke="#b7bccb" stroke-width="1"><circle cx="5" cy="5" r="4"/><path d="M5 2.5v5M6.3 3.6H4.5a.9.9 0 0 0 0 1.8h1a.9.9 0 0 1 0 1.8H3.7"/></svg>£30,000 – £36,000</div>
      <div class="apply">Apply Now</div></div>
  </div>
</section>

<section class="benefits">
  <div class="wrap">
    <div class="ben-left">
      <div class="eyebrow">WHY REGISTER</div>
      <h2 class="sec-title">Benefits of Joining Our Talent Pool</h2>
      <ul class="ben-list">
        <li><span class="tick"><svg width="9" height="9" viewBox="0 0 10 10" fill="none" stroke="#c9940f" stroke-width="1.3"><path d="m2 5.2 2 2L8 3"/></svg></span><div><h3>Matched to the Right Role</h3><p>Our consultants take time to understand your skills, experience and preferences — no generic job blasts.</p></div></li>
        <li><span class="tick"><svg width="9" height="9" viewBox="0 0 10 10" fill="none" stroke="#c9940f" stroke-width="1.3"><path d="m2 5.2 2 2L8 3"/></svg></span><div><h3>Access to Hidden Vacancies</h3><p>Many of our client roles are never publicly advertised. Registered candidates get first access.</p></div></li>
        <li><span class="tick"><svg width="9" height="9" viewBox="0 0 10 10" fill="none" stroke="#c9940f" stroke-width="1.3"><path d="m2 5.2 2 2L8 3"/></svg></span><div><h3>Free Career Support</h3><p>CV reviews, interview coaching and career guidance — all included when you register with us.</p></div></li>
        <li><span class="tick"><svg width="9" height="9" viewBox="0 0 10 10" fill="none" stroke="#c9940f" stroke-width="1.3"><path d="m2 5.2 2 2L8 3"/></svg></span><div><h3>Fast-Track Placement</h3><p>With your details on file, we can put you forward the moment a matching role comes in.</p></div></li>
        <li><span class="tick"><svg width="9" height="9" viewBox="0 0 10 10" fill="none" stroke="#c9940f" stroke-width="1.3"><path d="m2 5.2 2 2L8 3"/></svg></span><div><h3>Multiple Sectors</h3><p>Oil &amp; Gas, Construction, Warehouse, Manufacturing, Admin — one registration covers all.</p></div></li>
      </ul>
    </div>
    <div class="ben-photo" role="img" aria-label="Overhead photo of a white desk with a person typing on a laptop, a coffee cup, a tablet and a notepad"></div>
  </div>
</section>

<section class="cta">
  <h2>Ready to Start Your Job Search?</h2>
  <p>Register today. Our consultants are standing by to match you with live vacancies in your sector.</p>
  <span class="btn btn-hero">Register Now
    <svg width="10" height="10" viewBox="0 0 10 10" fill="none" stroke="currentColor" stroke-width="1.4"><path d="M1 5h8M5.8 1.8 9 5 5.8 8.2"/></svg>
  </span>
</section>

<footer class="footer">
  <div class="wrap">
    <div class="foot-cols">
      <div>
        <div class="foot-brand"><span class="brand-dot"></span>Harborline</div>
        <p class="foot-about">Your trusted national recruitment partner connecting talent with opportunity.</p>
      </div>
      <div><h4>QUICK LINKS</h4><ul><li>Home</li><li>Sectors</li><li>About Us</li><li>Contact</li></ul></div>
      <div><h4>CANDIDATES</h4><ul><li>Browse Jobs</li><li>Submit CV</li><li>How It Works</li></ul></div>
      <div><h4>EMPLOYERS</h4><ul><li>Hire Staff</li><li>Solutions</li></ul></div>
    </div>
    <div class="foot-bottom">
      <div>© 2026 Harborline Recruitment. All rights reserved.</div>
      <div><span>Privacy Policy</span><span>Terms of Service</span></div>
    </div>
  </div>
</footer>

</body>
</html>
```